High-end residential home builder needs a business card design

We need a new business card design for a small residential construction company based in Boise, Idaho. We specialize in building custom high-end homes and remodels, with a focus on great design and craftsmanship.

We would like to use our current logo, but open to new color suggestions.
Just looking for a clean, sharp, modern design that looks high-end.

Target Market(s)

Upscale clientele

Industry/Entity Type

Contractor

Contact Information for Business Card

Company: Stonefield Custom Builders
Name: Marcus Tilley
Phone number: 208 367 4120
Email: MarcusTilleySCB@mailbox-example.com
Website: Stonefieldcustombuilders-example.com

Font styles to use
Serif
Sans Serif

Requirements
Must have
• Company Logo
Company name
My name
My phone number
My email
Company website
Nice to have
• I have attached a few photos of cards that I really like.

```html
<!DOCTYPE html>
<html lang="en">
<head>
<meta charset="utf-8">
<title>Stonefield Custom Builders – Business Card</title>
<link rel="stylesheet" href="https://fonts.googleapis.com/css2?family=Montserrat:wght@400;500;700&display=swap">
<style>
  :root {
    --page: #eeeeee;
    --card-dark: #0b0b0b;
    --card-mid: #1c1c1c;
    --ink: #ffffff;
    --ink-soft: #d9d9d9;
    --ink-muted: #8a8a8a;
    --rule: #9a9a9a;
  }
  * { box-sizing: border-box; margin: 0; padding: 0; }
  html, body { width: 1200px; height: 926px; overflow: hidden; }
  body {
    background: var(--page);
    font-family: "Montserrat", sans-serif;
    position: relative;
  }
  .card {
    position: absolute;
    width: 560px;
    height: 320px;
    background: radial-gradient(ellipse at 45% 35%, var(--card-mid) 0%, var(--card-dark) 70%);
    box-shadow: 0 10px 26px rgba(0,0,0,.22);
    overflow: hidden;
    color: var(--ink);
  }
  .card--front { left: 60px; top: 500px; }
  .card--back { left: 580px; top: 120px; }

  .card__band {
    position: absolute;
    left: 0; right: 0; bottom: 0;
    height: 34px;
  }
  .card__band::before {
    content: "";
    position: absolute;
    left: 34px; right: 0; top: 8px;
    height: 2px;
    background: var(--rule);
  }
  .card__band-mark {
    position: absolute;
    left: 12px; top: 3px;
    width: 12px; height: 12px;
    border: 1.5px solid var(--ink);
  }

  /* front */
  .brand {
    position: absolute;
    left: 40px; top: 80px;
    width: 200px;
    display: flex;
    flex-direction: column;
    align-items: center;
    gap: 14px;
  }
  .brand__square {
    width: 70px; height: 70px;
    border: 3px solid var(--ink);
  }
  .brand__name {
    font-weight: 500;
    font-size: 20px;
    letter-spacing: 4px;
    text-transform: uppercase;
    color: var(--ink);
  }
  .divider {
    position: absolute;
    left: 256px; top: 40px;
    width: 1px; height: 210px;
    background: linear-gradient(to bottom, transparent, var(--ink-soft), transparent);
    transform: rotate(18deg);
  }
  .contact {
    position: absolute;
    left: 300px; top: 92px;
    width: 250px;
  }
  .contact__name {
    font-weight: 700;
    font-size: 22px;
    letter-spacing: .5px;
    text-transform: uppercase;
  }
  .contact__role {
    font-weight: 500;
    font-size: 10.5px;
    letter-spacing: .6px;
    text-transform: uppercase;
    color: var(--ink-soft);
    margin-top: 3px;
    padding-bottom: 10px;
    border-bottom: 1px solid var(--rule);
  }
  .contact__list { list-style: none; margin-top: 12px; }
  .contact__item {
    display: flex;
    align-items: center;
    gap: 8px;
    font-size: 10.5px;
    color: var(--ink-soft);
    margin-bottom: 9px;
    white-space: nowrap;
  }
  .contact__item--phone { font-weight: 700; font-size: 12px; color: var(--ink); }
  .contact__icon { flex: 0 0 22px; width: 22px; height: 22px; }

  /* back */
  .wordmark {
    position: absolute;
    left: 0; right: 0; top: 110px;
    display: flex;
    flex-direction: column;
    align-items: center;
  }
  .wordmark__name {
    font-weight: 500;
    font-size: 26px;
    letter-spacing: 8px;
    text-transform: uppercase;
    color: var(--ink);
    padding-bottom: 8px;
    border-bottom: 1px solid var(--rule);
  }
  .wordmark__tag {
    margin-top: 8px;
    font-weight: 500;
    font-size: 13px;
    letter-spacing: 6px;
    text-transform: uppercase;
    color: var(--ink-muted);
  }
</style>
</head>
<body>

  <section class="card card--back" aria-label="Card back">
    <div class="wordmark">
      <div class="wordmark__name">Stonefield</div>
      <div class="wordmark__tag">Custom Builders</div>
    </div>
    <div class="card__band"><span class="card__band-mark"></span></div>
  </section>

  <section class="card card--front" aria-label="Card front">
    <div class="brand">
      <div class="brand__square"></div>
      <div class="brand__name">Stonefield</div>
    </div>
    <div class="divider"></div>
    <div class="contact">
      <h1 class="contact__name">Marcus Tilley</h1>
      <p class="contact__role">Stonefield Custom Builders</p>
      <ul class="contact__list">
        <li class="contact__item contact__item--phone">
          <svg class="contact__icon" viewBox="0 0 22 22" aria-hidden="true">
            <polygon points="11,1 20,6 20,16 11,21 2,16 2,6" fill="none" stroke="#fff" stroke-width="1.3"/>
            <path d="M7.5 7.5c.8-.8 1.5-.6 2 .2l.6 1c.3.5.2 1-.2 1.3l-.5.4c.5 1 1.3 1.8 2.3 2.3l.4-.5c.3-.4.8-.5 1.3-.2l1 .6c.8.5 1 1.2.2 2-1 1-3 .6-5-1.4s-2.4-4-1.4-5z" fill="#fff"/>
          </svg>
          208 367 4120
        </li>
        <li class="contact__item">
          <svg class="contact__icon" viewBox="0 0 22 22" aria-hidden="true">
            <polygon points="11,1 20,6 20,16 11,21 2,16 2,6" fill="none" stroke="#fff" stroke-width="1.3"/>
            <rect x="6" y="8" width="10" height="7" fill="none" stroke="#fff" stroke-width="1"/>
            <polyline points="6,8 11,12 16,8" fill="none" stroke="#fff" stroke-width="1"/>
          </svg>
          MarcusTilleySCB@mailbox-example.com
        </li>
        <li class="contact__item">
          <svg class="contact__icon" viewBox="0 0 22 22" aria-hidden="true">
            <polygon points="11,1 20,6 20,16 11,21 2,16 2,6" fill="none" stroke="#fff" stroke-width="1.3"/>
            <circle cx="11" cy="11" r="5" fill="none" stroke="#fff" stroke-width="1"/>
            <ellipse cx="11" cy="11" rx="2.2" ry="5" fill="none" stroke="#fff" stroke-width=".8"/>
            <line x1="6" y1="11" x2="16" y2="11" stroke="#fff" stroke-width=".8"/>
          </svg>
          Stonefieldcustombuilders-example.com
        </li>
      </ul>
    </div>
    <div class="card__band"><span class="card__band-mark"></span></div>
  </section>

</body>
</html>
```